Full Social Media Branding

We are in need of a complete social media branding for the following platforms:

- Linkwork: Business and Personal Profiles. The Business profile should have a logo picture and a header, while the personal profile will only have a header.

- Friendbook: Business page only, logo picture and header.

- Chirper: Same as Friendbook.

- Snapgram: Same as Friendbook.

We have attached our logo and would like you to incorporate its colours into the designs. Please remove the subtext under the logo.

You can use our website, www.brindlepartners.co.uk, as a reference for inspiration.

We are a Quantity Surveying company that also provides estimating services and printing services for Architectural drawings.

```html
<!DOCTYPE html>
<html lang="en">
<head>
<meta charset="utf-8">
<title>Brindle Partners – Social Media Banners</title>
<link href="https://fonts.googleapis.com/css2?family=Montserrat:wght@500;600;700&display=swap" rel="stylesheet">
<style>
  :root{
    --board:#dcdcde;
    --purple-light:#8a3dba;
    --purple:#6d27a0;
    --purple-deep:#4a1672;
    --ink:#0b0b0b;
    --white:#ffffff;
    --label:#6a6a6a;
    --mark-dark:#3a1258;
  }
  *{margin:0;padding:0;box-sizing:border-box}
  html,body{width:1200px;height:826px;overflow:hidden}
  body{
    background:var(--board);
    font-family:"Montserrat",Arial,sans-serif;
    position:relative;
  }
  .board-label{
    position:absolute;
    font-size:5px;
    font-weight:600;
    letter-spacing:.02em;
    color:var(--label);
    text-transform:uppercase;
  }
  .banner{
    position:absolute;
    box-shadow:3px 4px 8px rgba(0,0,0,.28);
  }
  .banner__photo{
    position:absolute;inset:0;
    background:
      linear-gradient(180deg,rgba(255,255,255,.06),rgba(0,0,0,.12)),
      linear-gradient(110deg,var(--purple-light) 0%,var(--purple) 45%,var(--purple-deep) 100%);
  }
  .brand{
    position:absolute;
    left:50%;
    transform:translateX(-50%);
    color:var(--white);
    font-size:var(--s);
    white-space:nowrap;
  }
  .brand__row{display:flex;align-items:center;gap:.45em}
  .brand__dot{
    width:2.3em;height:2.3em;border-radius:50%;
    background:var(--white);flex:none;
  }
  .brand__name{
    font-weight:600;
    line-height:1.05;
    letter-spacing:.02em;
    text-transform:uppercase;
  }
  .strip{position:absolute;left:0;right:0;bottom:0}
  .strip__rule{
    position:absolute;left:0;
    height:2px;background:var(--white);
  }
  .strip__bar{
    position:absolute;left:0;right:0;bottom:0;
    background:var(--ink);
  }
  .call{
    position:absolute;right:0;bottom:0;
    background:var(--ink);
    color:var(--white);
    font-weight:600;
    display:flex;align-items:center;justify-content:center;
    clip-path:polygon(6% 0,100% 0,100% 100%,0 100%);
    padding-left:5%;
    white-space:nowrap;
  }
  .avatar{
    position:absolute;
    border-radius:50%;
    background:var(--white);
    border:2px solid var(--ink);
    box-shadow:0 0 0 3px var(--white),2px 3px 8px rgba(0,0,0,.3);
    display:flex;align-items:center;justify-content:center;
    color:var(--mark-dark);
    font-size:var(--s);
  }
  .avatar .brand__dot{background:var(--purple)}
  .avatar .brand__row{gap:.35em}
</style>
</head>
<body>

  <p class="board-label" style="left:55px;top:77px">Linkwork Banner</p>
  <section class="banner" style="left:55.5px;top:96.75px;width:626px;height:157px">
    <div class="banner__photo" role="img" aria-label="Aerial city skyline photograph tinted purple"></div>
    <div class="brand" style="--s:22px;top:52px">
      <div class="brand__row"><span class="brand__dot"></span><span class="brand__name">Brindle<br>Partners</span></div>
    </div>
    <div class="strip" style="height:28px">
      <span class="strip__rule" style="width:66%;bottom:6px"></span>
      <span class="strip__bar" style="height:5px"></span>
      <div class="call" style="width:216px;height:28px;font-size:17px">Call : 0161 555 0148</div>
    </div>
  </section>
  <div class="avatar" style="--s:8px;left:103px;top:206px;width:94px;height:94px">
    <div class="brand__row"><span class="brand__dot"></span><span class="brand__name">Brindle<br>Partners</span></div>
  </div>

  <p class="board-label" style="left:55px;top:323px">Chirper Banner</p>
  <section class="banner" style="left:55.5px;top:340.5px;width:604.5px;height:201px">
    <div class="banner__photo" role="img" aria-label="Aerial city skyline photograph tinted purple"></div>
    <div class="brand" style="--s:24px;top:72px">
      <div class="brand__row"><span class="brand__dot"></span><span class="brand__name">Brindle<br>Partners</span></div>
    </div>
    <div class="strip" style="height:27px">
      <span class="strip__rule" style="width:70%;bottom:6px"></span>
      <span class="strip__bar" style="height:5px"></span>
      <div class="call" style="width:216px;height:27px;font-size:17px">Call : 0161 555 0148</div>
    </div>
  </section>
  <div class="avatar" style="--s:8px;left:98px;top:485px;width:94px;height:94px">
    <div class="brand__row"><span class="brand__dot"></span><span class="brand__name">Brindle<br>Partners</span></div>
  </div>

  <p class="board-label" style="left:55px;top:600px">Friendbook Banner</p>
  <section class="banner" style="left:55px;top:614px;width:343.5px;height:127.5px">
    <div class="banner__photo" role="img" aria-label="Aerial city skyline photograph tinted purple"></div>
    <div class="brand" style="--s:14px;top:50px">
      <div class="brand__row"><span class="brand__dot"></span><span class="brand__name">Brindle<br>Partners</span></div>
    </div>
    <div class="strip" style="height:17px">
      <span class="strip__rule" style="width:66%;bottom:4px;height:1.5px"></span>
      <span class="strip__bar" style="height:3px"></span>
      <div class="call" style="width:132px;height:17px;font-size:10px">Call : 0161 555 0148</div>
    </div>
  </section>
  <div class="avatar" style="--s:6px;left:65px;top:699px;width:68px;height:68px">
    <div class="brand__row"><span class="brand__dot"></span><span class="brand__name">Brindle<br>Partners</span></div>
  </div>

  <p class="board-label" style="left:719px;top:77px">Snapgram Banner</p>
  <section class="banner" style="left:721.5px;top:96.75px;width:428px;height:427px">
    <div class="banner__photo" role="img" aria-label="Aerial city skyline photograph tinted purple"></div>
    <div class="brand" style="--s:27px;top:178px">
      <div class="brand__row"><span class="brand__dot"></span><span class="brand__name">Brindle<br>Partners</span></div>
    </div>
    <div class="strip" style="height:27px">
      <span class="strip__rule" style="width:55%;bottom:6px"></span>
      <span class="strip__bar" style="height:5px"></span>
      <div class="call" style="width:216px;height:27px;font-size:17px">Call : 0161 555 0148</div>
    </div>
  </section>

</body>
</html>
```